Timber Ridge Land Services Business Cards

Need to create a business card with the company logo "Timber Ridge Land Services". The business will provide forestry mulching for land clearing and vegetation control, brush and small tree removal, wildlife habitat improvement and trail and property access creation.

```html
<!DOCTYPE html>
<html lang="en">
<head>
<meta charset="utf-8">
<title>Timber Ridge Land Services – Business Cards</title>
<link rel="stylesheet" href="https://fonts.googleapis.com/css2?family=Exo+2:ital,wght@0,700;1,800&family=Montserrat:wght@400;500;700;800&display=swap">
<style>
  :root {
    --backdrop: #7f918c;
    --forest-deep: #0c4529;
    --forest-mid: #1d6a3c;
    --forest-light: #4aa157;
    --leaf: #63bd69;
    --ink-green: #10583a;
    --band: #0d5c3a;
    --band-text: #6dc774;
    --white: #ffffff;
  }
  * { box-sizing: border-box; margin: 0; padding: 0; }
  html, body {
    width: 1200px;
    height: 1038px;
    overflow: hidden;
    background: var(--backdrop);
  }
  .canvas {
    position: relative;
    width: 1200px;
    height: 1038px;
  }
  .card {
    position: absolute;
    width: 640px;
    height: 366px;
    box-shadow: 0 14px 30px rgba(0, 0, 0, 0.25);
    overflow: hidden;
  }

  /* Front */
  .card-front {
    left: 140px;
    top: 110px;
    background: radial-gradient(ellipse at 45% 45%, var(--forest-deep) 0%, var(--forest-mid) 55%, var(--forest-light) 100%);
    display: flex;
    align-items: center;
    justify-content: center;
  }
  .front-brand {
    font-family: "Montserrat", sans-serif;
    font-weight: 800;
    font-size: 38px;
    line-height: 1.15;
    letter-spacing: 1px;
    text-transform: uppercase;
    color: var(--white);
    text-align: center;
  }

  /* Back */
  .card-back {
    left: 420px;
    top: 560px;
    background: var(--leaf);
    color: var(--ink-green);
  }
  .back-brand {
    position: absolute;
    left: 44px;
    top: 36px;
    font-family: "Montserrat", sans-serif;
    font-weight: 800;
    font-size: 19px;
    line-height: 1.2;
    text-transform: uppercase;
    letter-spacing: 0.5px;
    color: var(--ink-green);
  }
  .person {
    position: absolute;
    left: 44px;
    top: 104px;
    display: flex;
    align-items: baseline;
    gap: 12px;
  }
  .person-name {
    font-family: "Exo 2", sans-serif;
    font-style: italic;
    font-weight: 800;
    font-size: 38px;
    color: var(--ink-green);
  }
  .person-role {
    font-family: "Montserrat", sans-serif;
    font-weight: 500;
    font-size: 13px;
    letter-spacing: 1px;
    text-transform: uppercase;
  }
  .address {
    position: absolute;
    right: 40px;
    top: 112px;
    display: flex;
    gap: 10px;
    align-items: flex-start;
    font-family: "Montserrat", sans-serif;
    font-weight: 500;
    font-size: 15px;
    line-height: 1.3;
  }
  .divider {
    position: absolute;
    left: 44px;
    right: 40px;
    top: 178px;
    height: 1px;
    background: var(--ink-green);
    opacity: 0.6;
  }
  .contacts {
    position: absolute;
    left: 44px;
    top: 194px;
    list-style: none;
    font-family: "Montserrat", sans-serif;
    font-weight: 500;
    font-size: 16px;
  }
  .contacts li {
    display: flex;
    align-items: center;
    gap: 10px;
    margin-bottom: 8px;
  }
  .icon {
    width: 18px;
    height: 18px;
    flex: none;
  }
  .web-band {
    position: absolute;
    left: 0;
    right: 0;
    bottom: 0;
    height: 78px;
    background: var(--band);
    display: flex;
    align-items: center;
    justify-content: center;
  }
  .web-address {
    font-family: "Exo 2", sans-serif;
    font-style: italic;
    font-weight: 800;
    font-size: 30px;
    color: var(--band-text);
    letter-spacing: 0.5px;
  }
</style>
</head>
<body>
<main class="canvas">
  <section class="card card-front" aria-label="Business card front">
    <h1 class="front-brand">Timber Ridge<br>Land Services</h1>
  </section>

  <section class="card card-back" aria-label="Business card back">
    <p class="back-brand">Timber Ridge<br>Land Services</p>

    <div class="person">
      <span class="person-name">Mark Ellison</span>
      <span class="person-role">Manager</span>
    </div>

    <div class="address">
      <svg class="icon" viewBox="0 0 24 24" aria-hidden="true">
        <circle cx="12" cy="12" r="12" fill="var(--ink-green)"/>
        <path d="M12 5a4.5 4.5 0 0 0-4.5 4.5c0 3.4 4.5 9 4.5 9s4.5-5.6 4.5-9A4.5 4.5 0 0 0 12 5zm0 6.2a1.7 1.7 0 1 1 0-3.4 1.7 1.7 0 0 1 0 3.4z" fill="var(--leaf)"/>
      </svg>
      <span>240 Quarry Mill Rd.<br>Suite # 40112</span>
    </div>

    <div class="divider"></div>

    <ul class="contacts">
      <li>
        <svg class="icon" viewBox="0 0 24 24" aria-hidden="true">
          <circle cx="12" cy="12" r="12" fill="var(--ink-green)"/>
          <path d="M8.6 6.5l1.8-.4 1.1 2.8-1.3 1a7 7 0 0 0 3.9 3.9l1-1.3 2.8 1.1-.4 1.8c-.2.6-.7 1-1.3 1A10 10 0 0 1 7.6 7.8c0-.6.4-1.1 1-1.3z" fill="var(--leaf)"/>
        </svg>
        <span>224-555-0187</span>
      </li>
      <li>
        <svg class="icon" viewBox="0 0 24 24" aria-hidden="true">
          <circle cx="12" cy="12" r="12" fill="var(--ink-green)"/>
          <rect x="6" y="8" width="12" height="8.5" rx="1" fill="var(--leaf)"/>
          <path d="M6.5 8.6L12 12.8l5.5-4.2" fill="none" stroke="var(--ink-green)" stroke-width="1.3"/>
        </svg>
        <span>info@timberridgeland.com</span>
      </li>
    </ul>

    <div class="web-band">
      <span class="web-address">www.timberridgeland.com</span>
    </div>
  </section>
</main>
</body>
</html>
```